Business Card Design

We would like a business card that utilizes our current logo and keeps with the same feel - elegant and organic. Our farm isn't about mass production, it's about excellence, education, beautiful events and flowers - people, culture, and community.

Target Market(s)

Patrons to our farm who are interested in weddings, events, or our flowers and vegetables.

Contact Information for Business Card

Name, address, cell email (Danielle Hoskins, 2716 Wrenfield Rd, Alder Vale, CO 80000, cell 30.412.6638, email danielle@wrenfieldacres.com)

```html
<!DOCTYPE html>
<html lang="en">
<head>
<meta charset="utf-8">
<title>Wrenfield Acres — Business Card</title>
<link href="https://fonts.googleapis.com/css2?family=Open+Sans:wght@400&family=Mrs+Saint+Delafield&display=swap" rel="stylesheet">
<style>
  :root {
    --page: #ffffff;
    --sage: #748873;
    --ink: #ffffff;
    --leaf: rgba(205, 222, 200, 0.5);
    --leaf-fade: rgba(205, 222, 200, 0);
    --rule: rgba(255, 255, 255, 0.9);
    --rule-fade: rgba(255, 255, 255, 0);
  }
  * { margin: 0; padding: 0; box-sizing: border-box; }
  html, body {
    width: 1200px; height: 2548px; overflow: hidden;
    background: var(--page);
  }
  .canvas { position: relative; width: 1200px; height: 2548px; }

  .card {
    position: absolute; left: 214px;
    width: 776px; height: 444px;
    background: var(--sage);
    overflow: hidden;
    box-shadow: 0 14px 36px rgba(0, 0, 0, 0.28);
    font-family: "Open Sans", Arial, sans-serif;
    color: var(--ink);
  }
  .card--front { top: 1463px; }
  .card--back { top: 2003px; }

  .foliage { position: absolute; }
  .foliage--tl { left: 0; top: 0; width: 137px; height: 100px;
    background: radial-gradient(ellipse at 35% 35%, var(--leaf), var(--leaf-fade) 70%); }
  .foliage--br { left: 531px; top: 332px; width: 245px; height: 112px;
    background: radial-gradient(ellipse at 50% 45%, var(--leaf), var(--leaf-fade) 70%); }
  .foliage--tr { left: 636px; top: 0; width: 140px; height: 75px;
    background: radial-gradient(ellipse at 60% 40%, var(--leaf), var(--leaf-fade) 70%); }
  .foliage--bl { left: 0; top: 347px; width: 196px; height: 97px;
    background: radial-gradient(ellipse at 45% 50%, var(--leaf), var(--leaf-fade) 70%); }

  .rule { position: absolute; }
  .rule--h { height: 1.5px; }
  .rule--v { width: 1.5px; }
  .to-left { background: linear-gradient(to left, var(--rule), var(--rule-fade)); }
  .to-right { background: linear-gradient(to right, var(--rule), var(--rule-fade)); }
  .to-top { background: linear-gradient(to top, var(--rule), var(--rule-fade)); }
  .to-bottom { background: linear-gradient(to bottom, var(--rule), var(--rule-fade)); }

  .brand {
    position: absolute;
    font-weight: 400; letter-spacing: 0.05em;
    white-space: nowrap; line-height: 1;
  }
  .card--front .brand { left: 164px; top: 122px; font-size: 28px; }
  .card--back .brand { left: 0; width: 776px; top: 208px; font-size: 38px; text-align: center; }

  .holder {
    position: absolute; left: 164px; top: 208px;
    font-family: "Mrs Saint Delafield", cursive;
    font-size: 32px; line-height: 1; white-space: nowrap;
  }

  .contact { position: absolute; left: 164px; top: 245px; list-style: none; }
  .contact li {
    display: flex; align-items: center;
    height: 29px; font-size: 15px; white-space: nowrap;
  }
  .contact svg { width: 12px; height: 12px; margin-right: 18px; fill: var(--ink); flex: none; }

  .card--back .email {
    position: absolute; left: 0; width: 702px; top: 352px;
    text-align: center; font-size: 15px; line-height: 20px;
  }
</style>
</head>
<body>
<main class="canvas">

  <section class="card card--front" aria-label="Business card front">
    <div class="foliage foliage--tl" role="img" aria-label="Faint leafy branch decoration"></div>
    <div class="foliage foliage--br" role="img" aria-label="Faint leafy branch decoration"></div>

    <div class="rule rule--h to-left" style="left:556px; top:77px; width:144px;"></div>
    <div class="rule rule--v to-bottom" style="left:699px; top:77px; height:150px;"></div>
    <div class="rule rule--v to-top" style="left:75px; top:225px; height:143px;"></div>
    <div class="rule rule--h to-right" style="left:75px; top:366px; width:146px;"></div>

    <div class="brand">Wrenfield Acres</div>
    <div class="holder">Danielle Hoskins</div>
    <ul class="contact">
      <li>
        <svg viewBox="0 0 24 24" aria-hidden="true"><path d="M6.6 10.8a15.1 15.1 0 0 0 6.6 6.6l2.2-2.2c.3-.3.7-.4 1-.2 1.1.4 2.3.6 3.6.6.6 0 1 .4 1 1V20c0 .6-.4 1-1 1A17 17 0 0 1 3 4c0-.6.4-1 1-1h3.5c.6 0 1 .4 1 1 0 1.3.2 2.5.6 3.6.1.3 0 .7-.2 1z"/></svg>
        30.412.6638
      </li>
      <li>
        <svg viewBox="0 0 24 24" aria-hidden="true"><path d="M12 2a7 7 0 0 0-7 7c0 5.2 7 13 7 13s7-7.8 7-13a7 7 0 0 0-7-7zm0 9.5a2.5 2.5 0 1 1 0-5 2.5 2.5 0 0 1 0 5z"/></svg>
        2716 Wrenfield Rd, Alder Vale, CO 80000
      </li>
      <li>
        <svg viewBox="0 0 24 24" aria-hidden="true"><path d="M2 5h20v14H2z M2 5l10 8 10-8" fill="none" stroke="#fff" stroke-width="2"/><path d="M2 5h20l-10 8z"/></svg>
        danielle@wrenfieldacres.com
      </li>
    </ul>
  </section>

  <section class="card card--back" aria-label="Business card back">
    <div class="foliage foliage--tr" role="img" aria-label="Faint leafy branch decoration"></div>
    <div class="foliage foliage--bl" role="img" aria-label="Faint leafy branch decoration"></div>

    <div class="rule rule--h to-right" style="left:76px; top:77px; width:145px;"></div>
    <div class="rule rule--v to-bottom" style="left:76px; top:77px; height:145px;"></div>
    <div class="rule rule--v to-top" style="left:696px; top:222px; height:144px;"></div>
    <div class="rule rule--h to-left" style="left:551px; top:365px; width:146px;"></div>

    <div class="brand">Wrenfield Acres</div>
    <div class="email">danielle@wrenfieldacres.com</div>
  </section>

</main>
</body>
</html>
```